Report presentation for measurement or inline reports

First page of report. Our inline reporting will come in a maintenance map. We want a modern first page and a real eye-catcher for a new company based in the Netherlands called: RTP Luchtregeling B.V. We are a service company witch measures, balances and give advices at indoor climate HVAC installations. We would like to see designs that use the color blue. We deliver our services to different buildings: Hospitals, atractions, officebuildings, government buildings, swimming pools and schools. Our website: www.rtpl.nl
Updates

Can you all add the new logo please. The companyname is RTP Luchtregeling B.V.. In witch format can i retrieve the design?

Industry/Entity Type

It Company

Colors
0255a3
3176b5
85abd2
cedeed
eaf1f7
ffffff

Requirements
Must have
• Projectname; projectplace; Inline or measure report; date; logo; companyname. it must be easy printable so not to much colours.
• The companyname is: RTP Luchtregeling B.V.. Please add the name. A new logo is updated.
Nice to have
• Maybe some pictures from hvac installations, buildings or measure

```html
<!DOCTYPE html>
<html lang="nl">
<head>
<meta charset="utf-8">
<title>RTP Luchtregeling B.V. – Rapport voorblad</title>
<link rel="stylesheet" href="https://fonts.googleapis.com/css2?family=Arimo:wght@400;700&family=PT+Sans:wght@700&display=swap">
<style>
  :root {
    --brand-blue: #0a5fb0;
    --navy: #1e4670;
    --logo-blue: #1e4a8a;
    --sky-light: #eaf1f7;
    --sky-mid: #cedeed;
    --steel: #85abd2;
    --facade: #3176b5;
    --ink: #2b2b2b;
    --white: #ffffff;
  }
  html, body {
    margin: 0;
    padding: 0;
    overflow: hidden;
    background: var(--white);
  }
  .cover {
    position: relative;
    width: 930px;
    height: 1200px;
    overflow: hidden;
    background: var(--white);
    font-family: "Arimo", Arial, sans-serif;
  }
  .cover-art {
    position: absolute;
    inset: 0;
  }
  .field {
    position: absolute;
    left: 59px;
    margin: 0;
    color: var(--ink);
    white-space: nowrap;
  }
  .field--large {
    font-size: 27px;
    font-weight: 700;
  }
  .field--small {
    font-size: 16px;
  }
  .field--bold { font-weight: 700; }
  .project-name { top: 515px; }
  .project-place { top: 596px; }
  .report-type { top: 660px; }
  .report-date { top: 690px; }

  .brand-mark {
    position: absolute;
    left: 782px;
    top: 815px;
    width: 100px;
    height: 92px;
    background: var(--facade);
  }
  .brand-name {
    position: absolute;
    right: 22px;
    top: 914px;
    margin: 0;
    font-size: 15px;
    font-weight: 700;
    color: var(--logo-blue);
    white-space: nowrap;
  }
  .footer-name {
    position: absolute;
    left: 27px;
    top: 1136px;
    margin: 0;
    font-family: "PT Sans", Arial, sans-serif;
    font-size: 38px;
    font-weight: 700;
    color: var(--white);
    white-space: nowrap;
  }
</style>
</head>
<body>
<main class="cover">
  <svg class="cover-art" width="930" height="1200" viewBox="0 0 930 1200" aria-hidden="false">
    <defs>
      <linearGradient id="photo-tone" x1="0" y1="0" x2="0.4" y2="1">
        <stop offset="0" stop-color="#eaf1f7"/>
        <stop offset="0.3" stop-color="#b9c9de"/>
        <stop offset="0.55" stop-color="#5d6f8c"/>
        <stop offset="1" stop-color="#3a4660"/>
      </linearGradient>
      <clipPath id="photo-shape">
        <polygon points="263,0 930,0 930,272 549,890 0,713 0,436"/>
      </clipPath>
    </defs>

    <polygon class="corner-accent" points="0,0 263,0 0,436" fill="var(--brand-blue)"/>

    <g clip-path="url(#photo-shape)">
      <rect class="building-photo" x="0" y="0" width="930" height="900"
            fill="url(#photo-tone)" role="img"
            aria-label="Photo of a modern office building with a thermal camera overlay against a cloudy sky"/>
      <rect class="info-veil" x="0" y="475" width="930" height="430" fill="var(--white)" opacity="0.72"/>
    </g>

    <polygon class="footer-band" points="0,713 930,1012 930,1200 0,1200" fill="var(--navy)"/>
  </svg>

  <p class="field field--large project-name">Project name:</p>
  <p class="field field--large project-place">Project place:</p>
  <p class="field field--small field--bold report-type">Inline or measure report:</p>
  <p class="field field--small report-date">Date:</p>

  <div class="brand-mark"></div>
  <p class="brand-name">RTP Luchtregeling B.V.</p>

  <p class="footer-name">RTP Luchtregeling B.V.</p>
</main>
</body>
</html>
```